Business Card Design Project

I have established a company called "Tidewell" which is a business specialising in psychotherapy/counselling , predominantly for anxiety & depression.

My name is Mel....hence, the Tidewell link. However, Tidewell was also chosen for its reference to green shoots of growth/recovery.

Tidewell is to be "upmarket" and highly professional. I'm keen for the style and colours to reflect this.....taupe/grey with navy/black script, for example.....NO primary colours.

My name needs to be on the card and my mobile number. Not sure, but suspect it should also have my qualifications ( BA (Psych) & BSc (Hons) Psychology). Mobile number 0463 918 207.

```html
<!DOCTYPE html>
<html lang="en">
<head>
<meta charset="UTF-8">
<title>Tidewell – Business Card</title>
<link href="https://fonts.googleapis.com/css2?family=Quicksand:wght@300;400&family=Open+Sans:wght@400;600&display=swap" rel="stylesheet">
<style>
  :root {
    --backdrop: #1f2826;
    --panel-light: #e4e1da;
    --panel-mid: #aaa59b;
    --panel-dark: #4d4a45;
    --card-dark: #2a2927;
    --card-mid: #4a4743;
    --card-taupe: #8c867c;
    --card-light: #a9a398;
    --name-navy: #1c2746;
    --brand-sage: #3e4a2a;
    --text-dark: #121212;
    --text-light: #f4f2ee;
    --mark-tone: #d6cfbd;
  }
  html, body {
    margin: 0;
    padding: 0;
    width: 1200px;
    height: 1029px;
    overflow: hidden;
    background: var(--backdrop);
  }
  .card {
    position: absolute;
    left: 100px;
    top: 243px;
    width: 1000px;
    height: 543px;
    overflow: hidden;
    background: linear-gradient(100deg, var(--card-dark) 0%, var(--card-mid) 40%, var(--card-taupe) 72%, var(--card-light) 100%);
  }
  .card__texture {
    position: absolute;
    inset: 0 0 0 376px;
    background: linear-gradient(160deg, rgba(0,0,0,0.3) 0%, rgba(0,0,0,0) 55%, rgba(255,255,255,0.12) 100%);
  }
  .card__brand-panel {
    position: absolute;
    left: 0;
    top: 0;
    width: 376px;
    height: 543px;
    background: linear-gradient(90deg, var(--panel-light) 0%, var(--panel-mid) 45%, var(--panel-dark) 100%);
    display: flex;
    align-items: center;
    justify-content: center;
    gap: 18px;
  }
  .brand-mark__dot {
    width: 46px;
    height: 46px;
    border-radius: 50%;
    background: var(--mark-tone);
  }
  .brand-mark__name {
    font-family: "Quicksand", sans-serif;
    font-weight: 400;
    font-size: 50px;
    color: var(--text-dark);
  }
  .card__details {
    position: absolute;
    right: 62px;
    top: 88px;
    text-align: right;
  }
  .details__name {
    font-family: "Quicksand", sans-serif;
    font-weight: 300;
    font-size: 112px;
    line-height: 1;
    color: var(--name-navy);
    letter-spacing: 2px;
  }
  .details__brand {
    font-family: "Quicksand", sans-serif;
    font-weight: 400;
    font-size: 62px;
    line-height: 1;
    color: var(--brand-sage);
    margin-top: -8px;
    margin-bottom: 20px;
    letter-spacing: 1px;
  }
  .details__line {
    font-family: "Open Sans", sans-serif;
    font-weight: 400;
    font-size: 29px;
    line-height: 40px;
    color: var(--text-dark);
  }
  .details__line--mobile { margin-top: 10px; }
  .card__tagline {
    position: absolute;
    right: 62px;
    top: 475px;
    font-family: "Open Sans", sans-serif;
    font-weight: 400;
    font-size: 42px;
    color: var(--text-light);
  }
</style>
</head>
<body>
  <div class="card">
    <div class="card__texture" role="img" aria-label="Fine diagonal charcoal texture"></div>
    <div class="card__brand-panel">
      <span class="brand-mark__dot"></span>
      <span class="brand-mark__name">Tidewell</span>
    </div>
    <div class="card__details">
      <div class="details__name">MEL</div>
      <div class="details__brand">Tidewell</div>
      <div class="details__line">BA (Psych)</div>
      <div class="details__line">BSc (Hons) Psychology</div>
      <div class="details__line details__line--mobile">Mobile: 0463 918 207</div>
    </div>
    <div class="card__tagline">Specialising In Psychotherapy</div>
  </div>
</body>
</html>
```